BeLMoZ clinical trial results infographic

We need an infographic which presents the results from the BeLMoZ research trial. It should be colourful and engaging, in understandable language and showing the steps to get to the results. This is to showcase the results to patients/the public/clinicians, giving a brief summary of what the study proved. The final design should have the BeLMoZ logo at the top (please see the logo on the attached Word document)
I have attached the required logos which need to be used (BeLMoZ - within the Word doc, Pembury Injury and Urgent Care, University of Wrenford) as well as an example from another study, KWELLO3, as an example of what the layout could look like. Please DO NOT use the content from the KWELLO3 example though, please instead use the content from the attached document 'InfographicDesignInformation_BELMOZ_ArtPosse_02Dec2025'. Please also include information about the funding in a footer at the bottom of the infographic (as per the above document).

```html
<!DOCTYPE html>
<html lang="en">
<head>
<meta charset="utf-8">
<title>BELMOZ trial results</title>
<link href="https://fonts.googleapis.com/css2?family=Montserrat:wght@600;700;800&family=Open+Sans:wght@400;600;700&display=swap" rel="stylesheet">
<style>
  :root {
    --ink: #1b1e2c;
    --band: #20232f;
    --page: #eef0f4;
    --card: #ffffff;
    --accent: #e0685a;
    --muted: #5b6070;
    --navy: #0c2a5b;
  }
  * { box-sizing: border-box; margin: 0; padding: 0; }
  html, body { width: 845px; height: 1200px; overflow: hidden; }
  body { background: var(--page); font-family: "Open Sans", sans-serif; color: var(--ink); position: relative; }
  .poster { position: absolute; inset: 0; }

  .brand { position: absolute; left: 40px; top: 36px; display: flex; align-items: center; gap: 8px; }
  .brand-mark { width: 12px; height: 12px; background: var(--accent); }
  .brand-name { font-family: "Montserrat", sans-serif; font-weight: 800; font-size: 24px; color: var(--ink); }
  .brand-sub { position: absolute; left: 40px; top: 82px; width: 200px; font-size: 8px; font-weight: 700; letter-spacing: .5px; color: var(--muted); }

  .uni { position: absolute; right: 36px; top: 20px; width: 70px; text-align: center; }
  .uni-square { width: 56px; height: 56px; background: var(--navy); margin: 0 auto 4px; }
  .uni-name { font-weight: 600; font-size: 8px; color: var(--navy); line-height: 1.2; }

  .headline { position: absolute; left: 250px; top: 38px; width: 480px; text-align: center;
    font-family: "Montserrat", sans-serif; font-weight: 800; font-size: 17px; line-height: 1.3; text-transform: uppercase; }

  .label { font-family: "Montserrat", sans-serif; font-weight: 800; font-size: 12px; letter-spacing: .6px; text-transform: uppercase;
    color: #fff; background: var(--band); display: inline-block; padding: 6px 14px; }
  .section-band { position: absolute; left: 0; width: 845px; background: var(--band); color: #fff; }

  .summary { top: 170px; height: 220px; }
  .summary .label { position: absolute; left: 40px; top: 14px; background: var(--accent); }
  .summary-text { position: absolute; left: 40px; top: 52px; width: 420px; font-size: 10px; line-height: 1.55; color: #e7e9ef; }
  .summary-text p + p { margin-top: 6px; }
  .summary-art { position: absolute; left: 520px; top: 14px; width: 290px; height: 192px;
    background: linear-gradient(180deg, #f3e4dc, #d8b2a4); }

  .findings { position: absolute; left: 40px; top: 402px; width: 500px; }
  .findings p { margin-top: 8px; font-size: 10.5px; line-height: 1.5; }
  .findings-art { position: absolute; left: 580px; top: 398px; width: 230px; height: 64px;
    background: linear-gradient(90deg, #f2e6df, #e8a597); border-radius: 32px; }

  .elig-band { top: 472px; height: 28px; }
  .elig-band .label { padding: 7px 40px; }
  .criteria { position: absolute; top: 508px; width: 375px; }
  .criteria.included { left: 40px; }
  .criteria.excluded { left: 430px; }
  .criteria h3 { font-family: "Montserrat", sans-serif; font-weight: 700; font-size: 12px; margin-bottom: 10px; }
  .criteria-items { display: flex; gap: 16px; }
  .item { flex: 1; font-size: 9.5px; line-height: 1.45; text-align: center; }
  .item-art { height: 110px; margin-bottom: 8px; background: linear-gradient(180deg, #fbe9e4, #eeb6a9); border-radius: 6px; }
  .item-art.narrow { width: 70px; margin-left: auto; margin-right: auto; }
  .item b { color: var(--accent); }

  .details-band { top: 735px; height: 28px; }
  .details-band .label { padding: 7px 40px; }
  .detail { position: absolute; top: 780px; width: 370px; display: flex; gap: 14px; align-items: flex-start; font-size: 10px; line-height: 1.5; }
  .detail.design { left: 40px; }
  .detail.blinding { left: 430px; }
  .detail-art { flex: none; width: 110px; height: 150px; background: linear-gradient(180deg, #eef1f6, #c9cfdb); border-radius: 6px; }
  .detail p { padding-top: 30px; }

  .contact { position: absolute; left: 40px; top: 975px; width: 360px; }
  .contact h4 { font-family: "Montserrat", sans-serif; font-weight: 800; font-size: 14px; text-transform: uppercase; margin-bottom: 14px; }
  .contact-line { display: flex; align-items: center; gap: 8px; font-size: 12px; font-weight: 600; color: var(--accent); }
  .funding { position: absolute; left: 500px; top: 975px; width: 310px; font-size: 9.5px; line-height: 1.5; }
  .partner { margin-top: 14px; display: flex; align-items: center; gap: 8px; }
  .partner-dot { width: 18px; height: 18px; border-radius: 50%; background: var(--accent); }
  .partner-name { font-weight: 700; font-size: 13px; color: var(--ink); text-transform: uppercase; }
  .foot { position: absolute; left: 0; bottom: 0; width: 845px; height: 30px; background: var(--band); }
</style>
</head>
<body>
<main class="poster">
  <header>
    <div class="brand"><span class="brand-mark"></span><span class="brand-name">BELMOZ</span></div>
    <div class="brand-sub">TRIAL OF ACUTE FEMORAL FRACTURE FIXATION</div>
    <h1 class="headline">In operating on broken lower thighs, surgeons use a nail or a plate, and a future study could establish which implant has better outcomes</h1>
    <div class="uni"><div class="uni-square"></div><div class="uni-name">University of Wrenford</div></div>
  </header>

  <section class="section-band summary">
    <h2 class="label">Study summary</h2>
    <div class="summary-text">
      <p>Distal femur fractures (broken thigh bone just above the knee) occur mostly in older patients after a fall, and in younger men during major trauma such as traffic accidents.</p>
      <p>In this feasibility study comparing the use of two surgical implants, patients were treated with an intramedullary nail or with a locking plate fixed to the outside of the bone.</p>
      <p>A small number of patients was recruited. A process evaluation helped to explain that surgeons appeared to select the fitter patients for inclusion, and sometimes had a preference for either implant. Completion of data was lower than expected, so a larger study would need to recruit more widely and follow patients up more closely with shorter forms.</p>
    </div>
    <div class="summary-art" role="img" aria-label="X-ray illustration of lower legs showing nail and plate fixation"></div>
  </section>

  <section class="findings">
    <h2 class="label">Key messages/findings</h2>
    <p>A comparison study of nail versus plate in distal femur fractures is feasible, with simpler procedures and if the design can allow for surgeons' preferences.</p>
  </section>
  <div class="findings-art" role="img" aria-label="Illustration of a fractured thigh bone"></div>

  <section class="section-band elig-band"><h2 class="label">Eligibility criteria</h2></section>
  <div class="criteria included">
    <h3>Included</h3>
    <div class="criteria-items">
      <div class="item"><div class="item-art narrow" role="img" aria-label="Illustration of an adult patient"></div>aged <b>18 and over</b></div>
      <div class="item"><div class="item-art" role="img" aria-label="Illustration of a broken lower femur"></div>Fracture of the distal femur which the surgeon believed <b>would benefit from internal fixation</b></div>
    </div>
  </div>
  <div class="criteria excluded">
    <h3>Excluded patients with</h3>
    <div class="criteria-items">
      <div class="item"><div class="item-art" role="img" aria-label="Illustration of a knee joint replacement"></div>a knee or hip <b>arthroplasty requiring revision</b></div>
      <div class="item"><div class="item-art" role="img" aria-label="Illustration of a deformed thigh bone"></div>an arthroplasty or any existing femoral deformity that <b>precluded nail fixation</b></div>
    </div>
  </div>

  <section class="section-band details-band"><h2 class="label">Study details</h2></section>
  <div class="detail design">
    <div class="detail-art" role="img" aria-label="Illustration of patients taking part in a study"></div>
    <p>A randomised controlled feasibility study at seven public hospitals in England. 23 of 50 eligible patients were recruited (nail 11, plate 12).</p>
  </div>
  <div class="detail blinding">
    <div class="detail-art" role="img" aria-label="Illustration of a patient in a wheelchair"></div>
    <p>Participants were blinded to the allocation. Primary outcomes were recruitment rate and completion rate of a quality-of-life questionnaire at 4 months after surgery.</p>
  </div>

  <footer>
    <div class="contact">
      <h4>Contact information</h4>
      <div class="contact-line">
        <svg width="20" height="14" viewBox="0 0 20 14" aria-hidden="true"><rect x="1" y="1" width="18" height="12" rx="1.5" fill="none" stroke="#e0685a" stroke-width="1.6"/><path d="M1.5 2 L10 8 L18.5 2" fill="none" stroke="#e0685a" stroke-width="1.6"/></svg>
        pemburytrials@wrenford-study.org
      </div>
    </div>
    <div class="funding">
      <p>National Health Studies Council Technology Assessment (HS/4471/08); supported by the HSC Wrenford Clinical Research Centre</p>
      <div class="partner"><span class="partner-dot"></span><span class="partner-name">Pembury Injury and Urgent Care</span></div>
    </div>
    <div class="foot"></div>
  </footer>
</main>
</body>
</html>
```